Accounting firm needing business card / letterhead designed
Marcus T. Elbering, CPA
marcus@fernquill.com
www.fernquill.com
482 N Harlow Ave Dunmere, ND 43719
419-555-0172

```html
<!DOCTYPE html>
<html lang="en">
<head>
<meta charset="utf-8">
<title>Fernquill — Stationery</title>
<link rel="stylesheet" href="https://fonts.googleapis.com/css2?family=Cabin:wght@400;600;700&display=swap">
<style>
  :root {
    --backdrop: #c9c9c9;
    --paper: #f7f7f6;
    --navy: #38356f;
    --green: #8cc63f;
    --ink: #3b3970;
  }
  html, body {
    margin: 0;
    padding: 0;
    width: 1200px;
    height: 1000px;
    overflow: hidden;
    background: var(--backdrop);
    font-family: "Cabin", "Gill Sans", sans-serif;
    color: var(--ink);
  }
  .canvas {
    position: relative;
    width: 1200px;
    height: 1000px;
  }
  .sheet {
    position: absolute;
    background: var(--paper);
  }
  .wordmark {
    position: absolute;
    font-weight: 700;
    color: var(--navy);
    letter-spacing: 0.04em;
    line-height: 1;
    white-space: nowrap;
  }

  /* Letterhead */
  .letterhead {
    left: 479px;
    top: 110px;
    width: 524px;
    height: 742px;
  }
  .letterhead .wordmark {
    right: 32px;
    top: 64px;
    font-size: 28px;
  }
  .letterhead .signatory {
    position: absolute;
    left: 31px;
    top: 591px;
    font-size: 9.5px;
    font-weight: 700;
    letter-spacing: 0.12em;
    text-transform: uppercase;
    color: var(--navy);
  }
  .letterhead .rule {
    position: absolute;
    left: 0;
    top: 604px;
    width: 160px;
    height: 3px;
    background: var(--green);
  }
  .letterhead .contact {
    position: absolute;
    left: 31px;
    top: 622px;
    font-size: 8.5px;
    line-height: 10px;
    letter-spacing: 0.04em;
  }
  .letterhead .contact p { margin: 0; }
  .letterhead .contact .gap { margin-top: 11px; }

  /* Business cards */
  .card {
    width: 228px;
    height: 126px;
  }
  .card-front {
    left: 209px;
    top: 531px;
  }
  .card-front .wordmark {
    right: 20px;
    top: 17px;
    font-size: 14px;
  }
  .card-front .signatory {
    position: absolute;
    left: 14px;
    top: 66px;
    font-size: 5.5px;
    font-weight: 700;
    letter-spacing: 0.1em;
    text-transform: uppercase;
    color: var(--navy);
  }
  .card-front .rule {
    position: absolute;
    left: 0;
    top: 73px;
    width: 61px;
    height: 2px;
    background: var(--green);
  }
  .card-front .contact {
    position: absolute;
    left: 14px;
    top: 84px;
    font-size: 4.5px;
    line-height: 5.5px;
    letter-spacing: 0.03em;
  }
  .card-front .contact p { margin: 0; }
  .card-front .contact .gap { margin-top: 5px; }

  .card-back {
    left: 212px;
    top: 684px;
  }
  .card-back .wordmark {
    left: 0;
    right: 0;
    top: 51px;
    text-align: center;
    font-size: 17px;
  }
  .card-back .web {
    position: absolute;
    left: 0;
    right: 0;
    top: 105px;
    text-align: center;
    font-size: 4.5px;
    letter-spacing: 0.05em;
  }
</style>
</head>
<body>
<main class="canvas">

  <section class="sheet letterhead" aria-label="Letterhead">
    <div class="wordmark">FERNQUILL</div>
    <div class="signatory">Marcus T. Elbering, CPA</div>
    <div class="rule"></div>
    <div class="contact">
      <p>555-555-0172</p>
      <p class="gap">marcus@fernquill.com</p>
      <p>www.fernquill.com</p>
      <p class="gap">482 N Harlow Ave Dunmere, ND 43719</p>
    </div>
  </section>

  <section class="sheet card card-front" aria-label="Business card front">
    <div class="wordmark">FERNQUILL</div>
    <div class="signatory">Marcus T. Elbering, CPA</div>
    <div class="rule"></div>
    <div class="contact">
      <p>555-555-0172</p>
      <p class="gap">marcus@fernquill.com</p>
      <p>www.fernquill.com</p>
      <p class="gap">482 N Harlow Ave Dunmere, ND 43719</p>
    </div>
  </section>

  <section class="sheet card card-back" aria-label="Business card back">
    <div class="wordmark">FERNQUILL</div>
    <div class="web">www.fernquill.com</div>
  </section>

</main>
</body>
</html>
```